Create Premium Wine Label Design

We are premium wine exporters from Australia. We are looking to introduce new brand " The Velloro" - in red wine, White wine and Sparkling wine to international market.

The sample label design for red wine ( Shiraz) is attached.

This is our luxury brand. We need a stunning wine label designs for (front, back and neck) that should be mostly in GOLD colour and design should be really eye catching.

We have provided sample design for front, back and neck labels. However, we are looking forward to see a completely new improvised design.

LOGO attached.

Front Label Design Specification:

* We would like to see designs that are in Gold colour.
* Wine Bottle size is standard: 750ml; we assume the same design can be resizable to different bottle sizes.
* Our design should suit both black, white and sparkling wine bottles(sample attached)
* Use our logo in the design (see attached - label sample)
* Content for front label (see attached).
* Design should include all information specified in the sample

Back Label Design
* All contents in the sample should be used ( sample attached)
* LOGO attached.

Neck Label Design
* Sample of Neck label attached, please provide similar or your own design.
* LOGO attached.

Image Samples:
* Samples of label designs we like (see attached)
* Sample for gold color (see attached)
* For bottle shapes (see attached)
* Front, Back and Neck Label Samples (see attached)

Target Market(s)

International Wine Market

Font styles to use
Decorative
Script

Requirements
Must have
• Must have golden color on front and back label

```html
<!DOCTYPE html>
<html lang="en">
<head>
<meta charset="utf-8">
<title>The Velloro – Label Set</title>
<link href="https://fonts.googleapis.com/css2?family=Poiret+One&family=Marcellus&family=Playfair+Display:wght@700;900&family=Cinzel:wght@500&display=swap" rel="stylesheet">
<style>
  :root {
    --navy: #1e2a34;
    --navy-deep: #17212a;
    --gold: #d4a437;
    --gold-light: #f1cf6a;
    --gold-dark: #9c7420;
    --ivory: #f2f2ee;
    --page: #ffffff;
    --neck-black: #111417;
  }
  * { box-sizing: border-box; margin: 0; padding: 0; }
  html, body { width: 1098px; height: 1200px; overflow: hidden; background: var(--page); }
  .canvas { position: relative; width: 1098px; height: 1200px; }

  /* shared label skin */
  .label {
    position: absolute;
    background:
      repeating-linear-gradient(115deg, rgba(255,255,255,0.025) 0 2px, transparent 2px 9px),
      linear-gradient(160deg, var(--navy) 0%, var(--navy-deep) 100%);
    overflow: hidden;
  }
  .gold-band {
    position: absolute; left: 0; right: 0; height: 10px;
    background: linear-gradient(90deg, var(--gold-dark), var(--gold-light) 35%, var(--gold) 60%, var(--gold-dark));
  }
  .gold-band.top { top: 0; }
  .gold-band.bottom { bottom: 0; }
  .pattern-strip {
    position: absolute; left: 0; top: 18px; bottom: 18px;
    background: linear-gradient(180deg, #2a3440 0%, #3a3a30 50%, #2a3440 100%);
  }
  .brand {
    position: absolute; right: 24px; text-align: center;
    font-family: "Cinzel", serif; font-weight: 500; color: var(--gold);
    letter-spacing: 2px;
  }
  .brand-dot {
    display: block; margin: 0 auto 8px; border-radius: 50%;
    background: var(--gold);
  }
  .title-the, .title-name {
    position: absolute; right: 24px; text-align: right;
    font-family: "Poiret One", sans-serif; color: var(--gold); line-height: 1;
  }
  .varietal {
    position: absolute; right: 24px; text-align: right;
    font-family: "Marcellus", serif; color: var(--ivory); letter-spacing: 1px; line-height: 1;
  }
  .vintage {
    position: absolute; right: 24px; text-align: right;
    font-family: "Playfair Display", serif; font-weight: 900; color: var(--gold); line-height: 1;
  }
  .origin {
    position: absolute; right: 24px; text-align: right;
    font-family: "Marcellus", serif; color: var(--gold);
    border-top: 1px solid var(--gold); padding-top: 6px;
  }

  /* still wine front label */
  .front-still { left: 70px; top: 210px; width: 440px; height: 920px; }
  .front-still .pattern-strip { width: 175px; }
  .front-still .brand { top: 96px; width: 200px; font-size: 20px; }
  .front-still .brand-dot { width: 26px; height: 26px; }
  .front-still .title-the { top: 300px; font-size: 80px; }
  .front-still .title-name { top: 388px; font-size: 74px; }
  .front-still .varietal { top: 590px; font-size: 50px; }
  .front-still .vintage { top: 735px; font-size: 70px; }
  .front-still .origin { top: 818px; width: 190px; font-size: 16px; }

  /* sparkling front label */
  .front-sparkling { left: 570px; top: 320px; width: 470px; height: 530px; }
  .front-sparkling .pattern-strip { width: 150px; }
  .front-sparkling .brand { top: 50px; width: 190px; font-size: 17px; }
  .front-sparkling .brand-dot { width: 22px; height: 22px; }
  .front-sparkling .title-the { top: 160px; font-size: 52px; }
  .front-sparkling .title-name { top: 220px; font-size: 64px; }
  .front-sparkling .varietal { top: 330px; font-size: 38px; }
  .front-sparkling .vintage { top: 400px; font-size: 50px; }
  .front-sparkling .origin { top: 462px; width: 150px; font-size: 12px; }

  /* neck label */
  .neck {
    position: absolute; left: 570px; top: 120px; width: 470px; height: 130px;
    background: var(--neck-black);
  }
  .neck .gold-band { height: 6px; }
  .neck-brand {
    position: absolute; left: 0; right: 0; top: 30px; text-align: center;
    font-family: "Cinzel", serif; font-weight: 500; font-size: 30px;
    letter-spacing: 3px; color: var(--gold);
  }
  .neck-flourish {
    position: absolute; left: 150px; width: 170px; top: 82px; height: 14px;
    border-radius: 7px;
    background: linear-gradient(90deg, transparent, var(--gold) 30%, var(--gold-light) 50%, var(--gold) 70%, transparent);
    opacity: 0.8;
  }
</style>
</head>
<body>
<main class="canvas">

  <section class="label front-still" aria-label="Still wine front label">
    <div class="gold-band top"></div>
    <div class="pattern-strip" role="img" aria-label="Gold lattice pattern panel"></div>
    <div class="brand"><span class="brand-dot"></span>MARROWIND</div>
    <div class="title-the">The</div>
    <div class="title-name">VELLORO</div>
    <div class="varietal">SIRAZ</div>
    <div class="vintage">2018</div>
    <div class="origin">WINE OF AUSTRALIA</div>
    <div class="gold-band bottom"></div>
  </section>

  <section class="neck" aria-label="Neck label">
    <div class="gold-band top"></div>
    <div class="neck-brand">MARROWIND</div>
    <div class="neck-flourish" role="img" aria-label="Gold scroll ornament"></div>
    <div class="gold-band bottom"></div>
  </section>

  <section class="label front-sparkling" aria-label="Sparkling wine front label">
    <div class="gold-band top"></div>
    <div class="pattern-strip" role="img" aria-label="Gold lattice pattern panel"></div>
    <div class="brand"><span class="brand-dot"></span>MARROWIND</div>
    <div class="title-the">The</div>
    <div class="title-name">VELLORO</div>
    <div class="varietal">SIRAZ</div>
    <div class="vintage">2018</div>
    <div class="origin">WINE OF AUSTRALIA</div>
    <div class="gold-band bottom"></div>
  </section>

</main>
</body>
</html>
```